User-interface and web design for new forum-style communication platform

We developed a new forum-style communication platform specially targetting stock investors to share and discuss information on companies listed on the stock exchange.

You have complete freedom for designing the user-interface and web design. Designs should include all features listed below.

Please read the attached document for full specifications. Also attached is a mockup of the layout, but this is only directional. A mockup for the user-profile is also attached, but does not need to be designed.

This project focusses on the homepage and thread view.

The winner(s) will be asked to design the complete project. (create thread box, user profile, registering, settings...)

We are looking for a well thought out, smart design that incorporates the specifications in the attached document. Please do not hesitate to contact us if anything is not clear.

Target Market(s)

Stock investors from 25 to 60 years old (the people that are currently on investor forums)

Industry/Entity Type

Communication

Font styles to use
Sans Serif

Colors

Designer to choose colors to be used in the design.

Requirements
Must have
• Full homepage design & Thread view specified in the attached document.
Nice to have
• Create thread view
- Field for adding tags
- field for subject of the thread
- text box with basic text editing
- method for sharing media
Should not have
• Logo design.

```html
<!DOCTYPE html>
<html lang="en">
<head>
<meta charset="utf-8">
<title>Investor Forum – Thread View</title>
<link rel="stylesheet" href="https://fonts.googleapis.com/css2?family=Arimo:wght@400;700&family=Open+Sans:wght@600;700&display=swap">
<style>
:root{
  --page-bg:#e8e9ea;
  --panel-bg:#ffffff;
  --frame:#3a7fc0;
  --field-border:#a9abad;
  --brand:#2f6db5;
  --accent:#3a87c4;
  --link:#1a73c9;
  --text:#111111;
  --muted:#333333;
  --badge:#e8806e;
  --avatar-top:#d2d3d4;
  --avatar-bottom:#bfc0c1;
}
*{box-sizing:border-box;margin:0;padding:0}
html,body{width:1200px;height:894px;overflow:hidden}
body{background:var(--page-bg);font-family:"Arimo",Arial,sans-serif;color:var(--text);position:relative}
a{text-decoration:none;color:inherit}

.brand-name{position:absolute;left:76px;top:35px;font-size:26px;font-weight:700;color:var(--brand);letter-spacing:.5px}
.top-search{position:absolute;left:316px;top:29px;width:457px;height:35px;background:var(--panel-bg);border:1px solid var(--field-border)}
.btn{position:absolute;top:29px;width:73px;height:34px;background:var(--accent);color:#fff;border-radius:3px;
  font-family:"Open Sans",Arial,sans-serif;font-weight:700;font-size:17px;display:flex;align-items:center;justify-content:center;padding-bottom:2px}
.btn-save{left:793px}.btn-clear{left:871px}
.notify-badge{position:absolute;left:984px;top:31px;width:27px;height:27px;border-radius:50%;background:var(--badge);color:#fff;
  font-family:"Open Sans",Arial,sans-serif;font-weight:700;font-size:14px;display:flex;align-items:center;justify-content:center}
.user-menu{position:absolute;left:1024px;top:30px;width:75px;height:28px;background:var(--panel-bg);border:1px solid var(--field-border);
  font-size:13px;padding:6px 0 0 10px}
.user-menu svg{position:absolute;right:10px;top:8px}

.side-box{position:absolute;left:56px;width:206px;background:var(--panel-bg);border:1px solid var(--frame);padding:13px 0 0 13px}
.side-box h2{font-size:14px;font-weight:700;margin-bottom:18px}
.side-box ul{list-style:none;margin-left:8px}
.side-box li{font-size:13px;color:var(--accent);height:24px}
.side-box .show-all{display:block;margin-top:11px;font-size:13px;font-weight:700;color:var(--link)}
.box-users{top:95px;height:96px}
.box-users h2{margin-bottom:14px}
.box-filters{top:195px;height:167px}
.box-tags{top:366px;height:167px}
.box-contrib{top:537px;height:167px}
.side-search{width:168px;height:35px;border:1px solid var(--field-border);font-size:13px;padding:11px 0 0 9px;position:relative;color:var(--muted)}
.side-search svg{position:absolute;right:10px;top:7px}

.breadcrumb{position:absolute;left:329px;top:89px;font-size:12px;color:var(--accent)}
.breadcrumb span{margin:0 6px}
.tabs{position:absolute;left:329px;top:129px;display:flex;align-items:center}
.tab-active{width:71px;height:26px;background:var(--accent);color:#fff;font-size:12px;font-weight:700;display:flex;align-items:center;justify-content:center}
.tab{font-size:12px;font-weight:700;margin-left:15px}

.avatar-fill{background:linear-gradient(180deg,var(--avatar-top),var(--avatar-bottom))}
.post{position:absolute;left:328px;width:771px;height:227px;background:var(--panel-bg);border:1px solid var(--frame)}
.post-1{top:185px}.post-2{top:535px}
.post .avatar{position:absolute;left:19px;top:20px;width:82px;height:82px}
.post .subject{position:absolute;left:118px;top:24px;font-size:14px;font-weight:700}
.post .meta{position:absolute;left:118px;top:49px;font-size:11px;color:var(--muted)}
.post .meta b{color:var(--link)}
.post .body{position:absolute;left:117px;top:77px;width:612px;font-size:12px;line-height:18px}
.post .stats{position:absolute;left:116px;top:182px;font-size:11px}
.post .stats a{color:var(--link);font-weight:700;margin-right:22px}
.post .actions{position:absolute;right:39px;top:202px;font-size:11px;font-weight:700;color:var(--link)}
.post .actions span{color:var(--muted);font-weight:400;margin:0 6px}

.reply-avatar{position:absolute;left:339px;width:82px;height:82px}
.reply-field{position:absolute;left:429px;width:671px;background:var(--panel-bg);border:1px solid var(--frame);font-size:12px;padding:19px 0 0 14px}
.reply-1 .reply-avatar{top:419px}.reply-1 .reply-field{top:419px;height:83px}
.reply-2 .reply-avatar{top:769px}.reply-2 .reply-field{top:776px;height:70px;padding-top:12px}
</style>
</head>
<body>

<header>
  <div class="brand-name">LOGO</div>
  <div class="top-search"></div>
  <a class="btn btn-save">Save</a>
  <a class="btn btn-clear">Clear</a>
  <div class="notify-badge">3</div>
  <div class="user-menu">user
    <svg width="14" height="10" viewBox="0 0 14 10"><path d="M1.5 1.5 L7 7.5 L12.5 1.5" fill="none" stroke="#111" stroke-width="3"/></svg>
  </div>
</header>

<aside>
  <section class="side-box box-users">
    <h2>Users</h2>
    <div class="side-search">Search
      <svg width="20" height="20" viewBox="0 0 20 20"><circle cx="8" cy="8" r="6" fill="none" stroke="#111" stroke-width="2.5"/><path d="M12.5 12.5 L18 18" stroke="#111" stroke-width="3" stroke-linecap="round"/></svg>
    </div>
  </section>
  <section class="side-box box-filters">
    <h2>Saved Filters</h2>
    <ul><li>Tech Earnings</li><li>Dividend Stocks</li><li>Small Caps</li></ul>
    <a class="show-all">show all</a>
  </section>
  <section class="side-box box-tags">
    <h2>Popular Tags</h2>
    <ul><li>#veltrax</li><li>#earnings</li><li>#dividends</li></ul>
    <a class="show-all">show all</a>
  </section>
  <section class="side-box box-contrib">
    <h2>Popular Contributors</h2>
    <ul><li>Marten</li><li>Ilse V.</li><li>Jorrit B.</li></ul>
    <a class="show-all">show all</a>
  </section>
</aside>

<main>
  <nav class="breadcrumb">Home<span>&gt;</span>Conversations<span>&gt;</span>Public<span>&gt;</span>#veltrax</nav>
  <div class="tabs"><div class="tab-active">Public</div><div class="tab">Following&nbsp; Contacts</div></div>

  <article class="post post-1">
    <div class="avatar avatar-fill" role="img" aria-label="Author profile photo"></div>
    <h3 class="subject">Veltrax Q3 results: margins under pressure?</h3>
    <p class="meta">Posted by <b>Marten</b> Fri on 01/01/2014 - 15:32</p>
    <p class="body">Veltrax reported third-quarter revenue slightly above consensus this morning, but gross margin slipped for the second quarter in a row as component costs kept rising. Management reaffirmed full-year guidance and announced a new share buyback of 200 million. I am curious how others read the call: is the margin dip temporary, or a sign that pricing power is fading? The stock is down four percent pre-market, which looks like an overreaction to me given the strong cash position and order backlog.</p>
    <p class="stats"><a>Read more</a>12 replies &nbsp; 250 views</p>
    <p class="actions">Reply<span>|</span>Share<span>|</span>Favourites</p>
  </article>
  <div class="reply-1">
    <div class="reply-avatar avatar-fill" role="img" aria-label="Your profile photo"></div>
    <div class="reply-field">Your reply here...</div>
  </div>

  <article class="post post-2">
    <div class="avatar avatar-fill" role="img" aria-label="Author profile photo"></div>
    <h3 class="subject">Dividend raise: what it means for long-term holders</h3>
    <p class="meta">Posted by <b>Marten</b> Fri on 01/01/2014 - 15:32</p>
    <p class="body">Alongside the results, the board raised the quarterly dividend by eight percent, the sixth increase in as many years. At the current price that puts the yield just under three percent, with a payout ratio still below half of free cash flow. For those of us holding for income this is welcome news, but I wonder whether the money would be better spent on research, given how fast competitors are moving. How are you positioning ahead of the next quarter, and are you adding on this dip or waiting?</p>
    <p class="stats"><a>Read more</a>12 replies &nbsp; 250 views</p>
    <p class="actions">Reply<span>|</span>Share<span>|</span>Favourites</p>
  </article>
  <div class="reply-2">
    <div class="reply-avatar avatar-fill" role="img" aria-label="Your profile photo"></div>
    <div class="reply-field">Your reply here...</div>
  </div>
</main>

</body>
</html>
```